Design and typesetting a NEVB report (approx 8-10 A4 pages)

We are a UK based ideas and innovation agency working within the UK Social Housing sector.
We have a report that needs designing up into an A4 PDF document that should run to about 8-10 A4 pages.
Design-wise we are looking for something dynamic with a housing and tech design theme. The document text is attached in the Word file.
Please find attached our logo and branding guidelines for font and logo use. We would be looking to use the main NEVB purple along with some NEW dynamic complimentary colours used throughout the design.
The report needs to read easily and cleanly so can be spaced out accordingly.
There will be on additional page of text to add at the back which we can send over once the successful candidate has been chosen.
Any questions please ask!
Target Market(s)
UK Social Housing sector
Industry/Entity Type
Social
Font styles to use
Other font styles liked:
- Gill Sans for body and Avant Garde for title (as specified in the attached branding guidelines)
Requirements
Must have
- Dynamic feel, stylish, colourful.
- Lots of space around the text.
Nice to have
- A bit of striking design work around the text (in the report template design)
Should not have
- Cluttered feel and fussy design.

```html
<!DOCTYPE html>
<html lang="en">
<head>
<meta charset="utf-8">
<title>NEVB Report – Is Housing Really Ready to Go Digital?</title>
<link href="https://fonts.googleapis.com/css2?family=Questrial&family=Lato:wght@300;400;700&display=swap" rel="stylesheet">
<style>
  :root {
    --backdrop: #aabfd2;
    --paper: #ffffff;
    --brand-purple: #5f4fae;
    --purple-soft: #b9b0e6;
    --rule-grey: #9a9a9a;
    --rule-light: #c7c7c7;
    --body-grey: #8a8a8a;
    --ink: #222222;
  }
  * { margin: 0; padding: 0; box-sizing: border-box; }
  html, body { width: 1200px; height: 1200px; overflow: hidden; }
  body { background: var(--backdrop); font-family: "Lato", sans-serif; position: relative; }

  .page {
    position: absolute; width: 323px; height: 457px;
    background: var(--paper);
    box-shadow: 0 10px 18px rgba(40, 60, 90, 0.28);
    overflow: hidden;
  }
  .col-1 { left: 94px; } .col-2 { left: 444px; } .col-3 { left: 797px; }
  .row-1 { top: 67px; } .row-2 { top: 629px; }

  .photo { position: absolute; left: 0; top: 0; width: 100%; }
  .photo-tall { height: 211px; }
  .photo-short { height: 127px; }
  .photo-edge { position: absolute; left: 0; top: 211px; width: 100%; height: 6px; background: var(--brand-purple); }

  /* cover */
  .cover-photo { height: 180px; background: radial-gradient(circle at 50% 55%, #6fb7d6 0%, #244a6a 38%, #0d1f30 80%); }
  .cover-band { position: absolute; top: 180px; left: 0; width: 100%; height: 13px; background: var(--rule-grey); }
  .cover-panel { position: absolute; top: 193px; left: 0; width: 100%; height: 168px; background: var(--brand-purple); }
  .cover-title {
    position: absolute; right: 29px; top: 98px; text-align: right;
    font-family: "Questrial", sans-serif; color: #fff; font-size: 19px; line-height: 23px; font-weight: 400;
  }
  .cover-sub {
    position: absolute; right: 29px; top: 146px;
    font-family: "Questrial", sans-serif; color: var(--purple-soft); font-size: 12px;
  }

  /* intro pages */
  .intro-text {
    position: absolute; left: 42px; top: 236px; width: 252px;
    border-left: 1px solid var(--rule-grey); padding-left: 9px;
    font-size: 7px; line-height: 13px; color: var(--body-grey); text-align: justify; font-weight: 300;
  }
  .intro-text p + p { margin-top: 13px; }

  /* list pages */
  .section-heading {
    position: absolute; left: 29px; top: 236px;
    font-family: "Questrial", sans-serif; color: var(--brand-purple); font-size: 12px; font-weight: 400;
  }
  .lead { position: absolute; left: 29px; top: 265px; font-size: 5.2px; color: var(--ink); }
  .points {
    position: absolute; left: 29px; width: 266px;
    font-size: 5.2px; line-height: 7.9px; color: var(--ink); text-align: justify;
  }
  .points li { margin-left: 10px; margin-bottom: 8px; }
  .points b { font-weight: 700; }
  .points-high { top: 281px; }
  .points-top { top: 157px; }

  /* footer */
  .footer-rule { position: absolute; top: 428px; height: 3px; background: var(--brand-purple); }
  .footer-rule::after { content: ""; position: absolute; left: 0; right: 0; top: 4px; height: 2px; background: var(--rule-light); }
  .rule-left { left: 0; width: 24px; }
  .rule-right { left: 100px; right: 0; }
  .brand {
    position: absolute; left: 30px; top: 417px;
    display: flex; align-items: center; gap: 6px;
    font-family: "Lato", sans-serif; font-weight: 400; font-size: 13px; line-height: 14px;
    color: var(--brand-purple); letter-spacing: 0.3px;
  }
  .brand-mark { width: 7px; height: 7px; background: var(--brand-purple); }
  .page-number {
    position: absolute; right: 16px; top: 413px; width: 14px; height: 14px;
    background: var(--brand-purple); color: #fff; font-size: 6px; line-height: 14px; text-align: center;
  }
</style>
</head>
<body>

<!-- Cover -->
<section class="page col-1 row-1">
  <div class="photo cover-photo" role="img" aria-label="Businessman holding a glowing holographic model house in his palm"></div>
  <div class="cover-band"></div>
  <div class="cover-panel">
    <h1 class="cover-title">Is Housing Really Ready<br>to Go Digital?</h1>
    <p class="cover-sub">— a manifesto for change</p>
  </div>
  <div class="footer-rule rule-left"></div><div class="footer-rule rule-right"></div>
  <div class="brand"><span class="brand-mark"></span>NEVB</div>
</section>

<!-- Page 2 -->
<section class="page col-2 row-1">
  <div class="photo photo-tall" role="img" aria-label="Suburban family house with porch and front lawn under a blue sky" style="background: linear-gradient(180deg, #2f8fe0 0%, #9fcdf0 35%, #8a8e96 60%, #5f8f3a 85%, #4c7a2c 100%);"></div>
  <div class="photo-edge"></div>
  <div class="intro-text">
    <p>The UK housing sector is stuck in a technology rut. Ubiquitous connectivity, machine learning and automation are transforming businesses across the economy, but social landlords remain wedded to systems and approaches which have successfully computerised the business practices of the 1960s and 1970s, but in too many areas have failed to move on.</p>
    <p>There is little evidence housing providers are capable of responding to the challenges and opportunities of a transformed digital world. At a time of rapidly falling budgets and the urgent need to reinvent business models, this represents a major unaddressed threat to the long term success of the sector.</p>
  </div>
  <div class="footer-rule rule-left"></div><div class="footer-rule rule-right"></div>
  <div class="brand"><span class="brand-mark"></span>NEVB</div>
  <div class="page-number">2</div>
</section>

<!-- Page 4 -->
<section class="page col-3 row-1">
  <div class="photo photo-short" role="img" aria-label="Modern white villa with swimming pool and palm trees in warm sunlight" style="background: linear-gradient(120deg, #f3dc7a 0%, #c7b25a 35%, #e8e2cf 60%, #7d8f4a 100%);"></div>
  <ol class="points points-top" start="3">
    <li><b>the barriers to change are too high and opportunities to innovate too few</b> – there are few examples of housing providers being willing to explore radical approaches to managing their stock outside conventional housing management paradigms, and where change is attempted the focus tends to be on making existing systems work slightly better, often by layering on more sub-optimal solutions, rather than reinventing them from scratch. The disruption becoming commonplace across the wider digital economy is largely missing from the housing sector, while boards still seek safety in digital strategies that embed existing business models.</li>
    <li><b>there is little or no understanding of technology issues on boards and senior teams</b> – driving the perception that technology is an area of risk and cost rather than opportunity. Lack of internal knowledge leads to an inadequate grasp of opportunities and problems, an over-reliance on expensive consultant-driven solutions, programmes that businesses cannot fully assess, a lack of organisational ambition in judging existing technology investment, and little appreciation of new solutions and approaches that might be out there.</li>
    <li><b>data ownership and governance are neglected issues across almost the entire housing sector</b> – with poor data practices endemic, a lack of integration between systems, little understanding or ownership of data at strategic or working levels, limited access to effective analytic tools and little opportunity to deploy them due to poor quality held data, so housing staff struggle to move their businesses forward and find it hard to gain traction and achieve significant results.</li>
  </ol>
  <div class="footer-rule rule-left"></div><div class="footer-rule rule-right"></div>
  <div class="brand"><span class="brand-mark"></span>NEVB</div>
  <div class="page-number">4</div>
</section>

<!-- Page 3 -->
<section class="page col-1 row-2">
  <div class="photo photo-tall" role="img" aria-label="Businessman with open hand beneath glowing internet of things icons" style="background: radial-gradient(circle at 60% 45%, #2fa7d8 0%, #143a5c 40%, #0a1526 85%);"></div>
  <div class="photo-edge"></div>
  <h2 class="section-heading">Five Big Failure Points</h2>
  <p class="lead">There are <b>five big failure points</b> in UK housing's approach to technology</p>
  <ol class="points points-high">
    <li><b>too often technology is seen as a service to the business and an operating cost to be managed rather than a key element of any business transformation strategy.</b> As a consequence, core housing management systems have increasingly become commoditised, with little to differentiate them and a focus on lowest price rather than best value for money. Businesses see IT as somehow separate from the business and digital as largely to do with minor changes to sustain existing sub-optimal processes, rather than a tool for more fundamental business reinvention.</li>
    <li><b>lack of competition and any significant pressure for business-focused innovation has led to an ecosystem defined by limited product differentiation, walled gardens and inaccessible APIs,</b> at a time when the wider digital economy is moving in the opposite direction, and at speed. Technology providers are not incentivised to innovate by clients who have little understanding of what might be achievable, and protect their business interests in other ways. This brings its own risk as inertia and long term revenue decline in the supplier market stalls innovation and threatens sustainability.</li>
  </ol>
  <div class="footer-rule rule-left"></div><div class="footer-rule rule-right"></div>
  <div class="brand"><span class="brand-mark"></span>NEVB</div>
  <div class="page-number">3</div>
</section>

<!-- Page 2 alternate -->
<section class="page col-2 row-2">
  <div class="photo photo-tall" role="img" aria-label="Hand touching a glowing house icon surrounded by a network of people icons" style="background: radial-gradient(circle at 50% 45%, #e8d8cc 0%, #b48a86 40%, #6e5a6a 80%, #4a4a52 100%);"></div>
  <div class="photo-edge"></div>
  <div class="intro-text">
    <p>The UK housing sector is stuck in a technology rut. Ubiquitous connectivity, machine learning and automation are transforming businesses across the economy, but social landlords remain wedded to systems and approaches which have successfully computerised the business practices of the 1960s and 1970s, but in too many areas have failed to move on.</p>
    <p>There is little evidence housing providers are capable of responding to the challenges and opportunities of a transformed digital world. At a time of rapidly falling budgets and the urgent need to reinvent business models, this represents a major unaddressed threat to the long term success of the sector.</p>
  </div>
  <div class="footer-rule rule-left"></div><div class="footer-rule rule-right"></div>
  <div class="brand"><span class="brand-mark"></span>NEVB</div>
  <div class="page-number">2</div>
</section>

<!-- Page 6 -->
<section class="page col-3 row-2">
  <div class="photo photo-short" role="img" aria-label="Warm lit modern living room with stone wall, sofa and dining chairs" style="background: linear-gradient(110deg, #8a6a3a 0%, #c9a25a 35%, #6e5a44 65%, #d8c8a8 100%);"></div>
  <ol class="points points-top" start="2">
    <li><b>to compensate for lack of internal strategic grip and understanding at Executive and Board levels, there is an over-reliance on external consultant-led change.</b> At their best this can help identify areas where businesses need to build their digital maturity and address the key issue of digital leadership capacity. However, it can also lead to hugely costly and time consuming exercises in rationalising and integrating existing systems and processes, when agile innovation and iterative transformation might be a more appropriate solution. This can be a fundamental weakness in how housing providers do tech and a major barrier to the adoption of effective approaches to digital transformation.</li>
    <li><b>finally, the lack of understanding of the value and use of data is a major issue at all levels in housing businesses.</b> Housing has a wealth of customer and customer related data and an unrivalled opportunity to connect it to other data available to the sector. But somehow the sector has failed to leverage this asset. Tales of poor quality customer data abound and all too often we hear of not knowing how many properties or having a complete record of customer information, at a level that is inconceivable in any comparable customer-focused business. The key to providing value and services is an intelligence-led business where marketing and sales is a high focus and businesses are transforming themselves by data-driven strategies based on accurate, real-time information: this is a gap where the sector needs to change its approach rapidly and radically.</li>
  </ol>
  <div class="footer-rule rule-left"></div><div class="footer-rule rule-right"></div>
  <div class="brand"><span class="brand-mark"></span>NEVB</div>
  <div class="page-number">6</div>
</section>

</body>
</html>
```